Personal informs intake and New Zealand divorce form automated filling service

I need a website that has a professional appearance, take information from clients, automatically fill New Zealand divorce forms based on information gathered. The personal information are listed:
Applicant’s information

1 First name

2 Middle name ( if Any )

3 Last name

4 Date of birth

5 Address

6 Email

7 Gender

8 Mobile

9 Occupation

10 Ethnicity

11 Country of residence

12 Do you live in New Zealand permanently?

13 Do you and your spouse have children who are under age 16 who require additional care?

Spouse’s information

1 Spouse’s first name

2 Spouse’s middle name ( if any )

3 Spouse’s last name

4 Spouse’s date of birth

5 Spouse’s occupation

6 Spouse’s ethnicity

7 Mobil number

8 Address

Marriage details

1 Did either party change their name by deed poll following the marriage/ civil union.

2 Date of marriage

3 Place and Address where the marriage was solemnized?

4 What date did you start living together?

5 What date did you cease living together?

6 How did you agree to separate? ( verbal agreement, written agreement, court order, or other )

The forms are New Zealand one party/joint application for Order dissolving a marriage or civil union.
Once the forms are completed, it will be checked by a human before sending to the paid clients by email. The website needs to integrate multiple mainstream payment options.

The forms are uploaded, please view it and set up the questionnaire accordingly to ensure all questions in the forms are answered. Must be able to distinguish one party or joint application.

Please contact me if you are interested and need more information.

Updated an AI generated draft as a sample

Target Market(s)

Divorcées

Coding

Coded - Design and coding required

Number of Pages Required

1 page

Font styles to use
Sans Serif

Colors

Designer to choose colors to be used in the design.

Requirements
Must have
• A professional appearance, easy to initiate the information intake process
Nice to have
• Step by step guideline, easy to understand how the website works
Should not have
• Bright colors

```html
<!DOCTYPE html>
<html lang="en">
<head>
<meta charset="utf-8">
<title>KiwiSplit — New Zealand Divorce Forms</title>
<link href="https://fonts.googleapis.com/css2?family=IBM+Plex+Sans:wght@400;500;600;700&family=Inter:wght@400;500;600&display=swap" rel="stylesheet">
<style>
:root{
  --navy:#1f2f4f;
  --navy-deep:#1c2a45;
  --ink:#1e2a3c;
  --muted:#4a5466;
  --soft:#f4f6f9;
  --card:#f1f3f7;
  --line:#e2e6ec;
  --green:#3fa56b;
  --white:#ffffff;
}
*{box-sizing:border-box;margin:0;padding:0}
html,body{width:1200px;height:3697px;overflow:hidden}
body{font-family:"Inter",sans-serif;color:var(--ink);background:var(--white)}
h1,h2,h3,.heading{font-family:"IBM Plex Sans",sans-serif}
section,header,footer{position:relative;width:1200px}
.center{text-align:center}
.btn{display:inline-flex;align-items:center;gap:8px;background:var(--navy);color:var(--white);border-radius:5px;font-size:11px;font-weight:500;padding:7px 12px;text-decoration:none}

/* nav */
.site-nav{height:50px;display:flex;align-items:center;padding:0 78px;border-bottom:1px solid var(--line)}
.brand{font-family:"IBM Plex Sans",sans-serif;font-weight:600;font-size:18px;color:var(--navy)}
.nav-links{display:flex;gap:30px;margin-left:auto;margin-right:auto;font-size:11px;font-weight:500;padding-left:150px}
.nav-links a{color:var(--ink);text-decoration:none}

/* hero */
.hero{height:622px;overflow:hidden;color:var(--white)}
.hero-photo{position:absolute;inset:0;background:radial-gradient(ellipse at 25% 35%,#3a4b68 0%,transparent 55%),linear-gradient(180deg,#27354f 0%,#1f2c45 60%,#1a2740 100%)}
.hero-inner{position:relative;padding-top:188px}
.hero h1{font-size:44px;font-weight:600;letter-spacing:-.3px}
.hero h1 span{color:#c9d3e3}
.hero .lead{font-size:18px;margin-top:16px;color:#eef1f6}
.hero .body{font-size:13.5px;line-height:19px;margin:20px auto 0;width:540px;color:#dfe4ec}
.hero-actions{display:flex;justify-content:center;gap:10px;margin-top:16px}
.hero-actions a{font-size:13px;padding:6px 12px;border-radius:5px;text-decoration:none;display:inline-flex;gap:8px;align-items:center}
.btn-light{background:var(--white);color:var(--ink)}
.btn-ghost{border:1px solid #e3e8f0;color:var(--white)}
.secure-note{font-size:10px;margin-top:22px;color:#d3d9e3;display:flex;justify-content:center;gap:6px;align-items:center}

/* process */
.process{height:414px;padding-top:64px}
.section-title{font-size:26px;font-weight:600;color:var(--ink)}
.steps{display:flex;justify-content:center;gap:0;margin-top:42px}
.step{width:210px;text-align:center}
.step-icon{width:40px;height:40px;border-radius:50%;background:var(--card);display:flex;align-items:center;justify-content:center;margin:0 auto}
.step-num{width:21px;height:21px;border-radius:50%;background:var(--navy);color:var(--white);font-size:11px;font-weight:600;display:flex;align-items:center;justify-content:center;margin:5px auto 0}
.step h3{font-family:"Inter",sans-serif;font-size:12.5px;font-weight:600;margin-top:12px}
.step p{font-size:10px;line-height:13.5px;color:var(--muted);margin:6px auto 0;width:190px}
.process .btn{margin-top:30px}

/* kiwis */
.kiwis{height:368px;background:var(--soft);padding-top:66px}
.kiwis p.intro{font-size:14px;line-height:19px;color:var(--muted);margin-top:14px}
.checklist{display:grid;grid-template-columns:347px 300px;column-gap:0;row-gap:18px;margin:34px 0 0 272px}
.checklist li{list-style:none;font-size:11px;color:var(--muted);display:flex;gap:8px;align-items:center}
.kiwis .btn{margin-top:38px}

/* accuracy */
.accuracy{height:564px;padding-top:62px}
.accuracy p.intro{font-size:14px;line-height:19px;color:var(--muted);margin-top:14px}
.accuracy .guided{font-size:13px;font-weight:600;margin-top:26px}
.form-row{display:flex;justify-content:center;gap:54px;margin-top:42px}
.form-row + .form-row{margin-top:42px}
.form-card{width:231px;height:84px;background:var(--card);border-radius:6px;padding:20px 22px;text-align:left}
.form-row.wide .form-card{width:250px;padding:20px 24px}
.form-row.wide{gap:36px}
.form-head{display:flex;align-items:center;gap:10px}
.tag{font-size:8px;background:var(--white);border:1px solid var(--line);border-radius:3px;padding:2px 6px;color:var(--muted)}
.form-code{font-size:13px;font-weight:600}
.form-desc{font-size:13px;color:var(--muted);margin-top:8px}
.accuracy .btn{margin-top:44px}

/* pricing */
.pricing{height:667px;background:var(--soft);padding-top:64px}
.plans{display:flex;justify-content:center;gap:27px;margin-top:42px}
.plan{width:327px;height:384px;background:var(--white);border:1px solid var(--line);border-radius:6px;box-shadow:0 2px 6px rgba(30,42,60,.08);text-align:center;padding-top:42px}
.plan.featured{border:2px solid var(--ink);box-shadow:none}
.plan h3{font-size:21px;font-weight:600}
.plan .for{font-size:11px;color:var(--muted);margin-top:8px}
.plan .price{font-family:"IBM Plex Sans",sans-serif;font-size:40px;font-weight:700;margin-top:10px}
.plan .fee{font-size:11px;color:var(--muted);margin-top:6px}
.plan .desc{font-size:13.5px;line-height:19px;color:var(--ink);margin:26px auto 0;width:250px;height:76px}
.plan .btn{font-size:12px;font-weight:600;padding:9px 15px;margin-top:26px}
.pay{font-size:13px;margin-top:44px;color:var(--ink)}
.pay strong{font-weight:600}
.ssl{font-size:11px;color:var(--muted);margin-top:8px;display:flex;justify-content:center;gap:6px;align-items:center}

/* faq */
.faq{height:416px;padding-top:64px}
.faq-list{width:537px;margin:28px auto 0}
.faq-item{border:1px solid var(--line);border-radius:6px;padding:12px 17px;margin-bottom:13px;box-shadow:0 1px 3px rgba(30,42,60,.05)}
.faq-q{display:flex;justify-content:space-between;align-items:center;font-size:10.5px;font-weight:600}
.faq-a{font-size:10px;line-height:14px;color:var(--muted);margin-top:12px}

/* contact */
.contact{height:350px;background:var(--soft);padding-top:70px}
.contact .sub{font-size:14px;color:var(--muted);margin-top:12px}
.contact-grid{display:flex;justify-content:center;gap:40px;margin-top:30px}
.contact-item{width:130px;text-align:center}
.contact-item svg{display:block;margin:0 auto}
.contact-item h4{font-size:11.5px;font-weight:600;margin-top:14px}
.contact-item p{font-size:11px;color:var(--muted);margin-top:10px}
.contact .btn{margin-top:30px}

/* footer */
.site-footer{height:246px;background:var(--navy-deep);color:var(--white);padding-top:48px}
.site-footer .brand{color:var(--white);font-size:17px;font-weight:500}
.foot-links{display:flex;justify-content:center;gap:23px;margin-top:22px;font-size:10px}
.foot-links a{color:#dbe0e8;text-decoration:none}
.foot-rule{width:1080px;height:1px;background:#34415c;margin:30px auto 0}
.copy{font-size:10px;color:#aab3c3;margin-top:28px}
.disclaimer{font-size:8.5px;color:#8c96a8;margin-top:8px}
</style>
</head>
<body>

<header class="site-nav">
  <div class="brand">KiwiSplit</div>
  <nav class="nav-links">
    <a href="#">Application</a><a href="#">How It Works</a><a href="#">FAQs</a><a href="#">Contact</a>
  </nav>
  <a class="btn" href="#">Start Your Application</a>
</header>

<section class="hero center">
  <div class="hero-photo" role="img" aria-label="Dim navy-toned photograph of the New Zealand Parliament buildings at dusk"></div>
  <div class="hero-inner">
    <h1>Dissolve Your Marriage, <span>the Right Way</span></h1>
    <p class="lead">A secure, professional divorce form service tailored for New Zealand law.</p>
    <p class="body">Whether filing alone or jointly, we guide you through every step—collect your details, generate your legally compliant application, and ensure every form is reviewed by a specialist before delivery.</p>
    <div class="hero-actions">
      <a class="btn-light" href="#">Begin Application
        <svg width="11" height="11" viewBox="0 0 12 12" fill="none" stroke="currentColor" stroke-width="1.3"><path d="M2 6h8M7 3l3 3-3 3"/></svg></a>
      <a class="btn-ghost" href="#">How It Works</a>
    </div>
    <p class="secure-note">
      <svg width="10" height="11" viewBox="0 0 10 11" fill="none" stroke="currentColor" stroke-width="1"><rect x="1.5" y="5" width="7" height="5" rx="1"/><path d="M3 5V3.5a2 2 0 0 1 4 0V5"/></svg>
      All data is encrypted and stored securely</p>
  </div>
</section>

<section class="process center">
  <h2 class="section-title">A Streamlined, Secure Process.</h2>
  <div class="steps">
    <div class="step">
      <div class="step-icon"><svg width="18" height="18" viewBox="0 0 18 18" fill="none" stroke="#334" stroke-width="1.2"><path d="M4 2h6l4 4v10H4z"/><path d="M10 2v4h4"/><circle cx="11" cy="12" r="1.6"/></svg></div>
      <div class="step-num">1</div>
      <h3>Answer a Secure Questionnaire</h3>
      <p>We collect essential information about you, your spouse, your marriage, and any children involved.</p>
    </div>
    <div class="step">
      <div class="step-icon"><svg width="18" height="18" viewBox="0 0 18 18" fill="none" stroke="#334" stroke-width="1.2"><circle cx="7" cy="6" r="3"/><path d="M2 15c0-3 2.5-5 5-5s5 2 5 5"/><path d="M11.5 3.2a3 3 0 0 1 0 5.6M13.5 10.5c1.5.7 2.5 2.4 2.5 4.5"/></svg></div>
      <div class="step-num">2</div>
      <h3>Select Your Application Type</h3>
      <p>Choose between a Joint Application (with spouse’s consent) or a One-Party Application (without).</p>
    </div>
    <div class="step">
      <div class="step-icon"><svg width="18" height="18" viewBox="0 0 18 18" fill="none" stroke="#334" stroke-width="1.2"><path d="M4 2h6l4 4v10H4z"/><path d="M10 2v4h4M6.5 9h5M6.5 12h5"/></svg></div>
      <div class="step-num">3</div>
      <h3>Auto-Fill Government Forms</h3>
      <p>Our system prepares all required documents based on your answers—accurately and efficiently.</p>
    </div>
    <div class="step">
      <div class="step-icon"><svg width="18" height="18" viewBox="0 0 18 18" fill="none" stroke="#334" stroke-width="1.2"><path d="M15.5 8.5A6.5 6.5 0 1 1 12 3"/><path d="M6 8.5l2.5 2.5L15.5 4"/></svg></div>
      <div class="step-num">4</div>
      <h3>Professional Review</h3>
      <p>A qualified expert checks your completed application before it’s sent to you.</p>
    </div>
    <div class="step">
      <div class="step-icon"><svg width="18" height="18" viewBox="0 0 18 18" fill="none" stroke="#334" stroke-width="1.2"><rect x="2" y="4" width="14" height="10" rx="1.5"/><path d="M2.5 5l6.5 5 6.5-5"/></svg></div>
      <div class="step-num">5</div>
      <h3>Receive Your Forms</h3>
      <p>You’ll receive your ready-to-file documents by email. Easy instructions included.</p>
    </div>
  </div>
  <a class="btn" href="#">Start Now- It’s Private &amp; Secure</a>
</section>

<section class="kiwis center">
  <h2 class="section-title">Created for Everyday Kiwis, Guided by the Law</h2>
  <p class="intro">Whether your separation was mutual or one-sided, our system helps you legally finalize<br>your marriage or civil union in New Zealand. We ensure every application meets Family Court standards.</p>
  <ul class="checklist">
    <li><svg width="15" height="15" viewBox="0 0 16 16" fill="none" stroke="var(--green)" stroke-width="1.4"><circle cx="8" cy="8" r="6.5"/><path d="M5 8.2l2 2 4-4.2"/></svg>New Zealand citizens and permanent residents</li>
    <li><svg width="15" height="15" viewBox="0 0 16 16" fill="none" stroke="var(--green)" stroke-width="1.4"><circle cx="8" cy="8" r="6.5"/><path d="M5 8.2l2 2 4-4.2"/></svg>Couples separated for over 2 years</li>
    <li><svg width="15" height="15" viewBox="0 0 16 16" fill="none" stroke="var(--green)" stroke-width="1.4"><circle cx="8" cy="8" r="6.5"/><path d="M5 8.2l2 2 4-4.2"/></svg>Individuals who can’t locate their spouse</li>
    <li><svg width="15" height="15" viewBox="0 0 16 16" fill="none" stroke="var(--green)" stroke-width="1.4"><circle cx="8" cy="8" r="6.5"/><path d="M5 8.2l2 2 4-4.2"/></svg>Parents needing to document child care arrangements</li>
  </ul>
  <a class="btn" href="#">Contact Us If You Have Questions</a>
</section>

<section class="accuracy center">
  <h2 class="section-title">Built for Accuracy. Backed by Legal Standards.</h2>
  <p class="intro">Every application follows the Family Proceedings Act 1980 and complies with New Zealand Family Court protocols.<br>We handle the technical paperwork—so you can focus on moving forward.</p>
  <p class="guided">You’ll be guided through all essential forms, including:</p>
  <div class="form-row">
    <div class="form-card"><div class="form-head"><span class="tag">▯ Form</span><span class="form-code">FP11 / FP13</span></div><div class="form-desc">Application for Order</div></div>
    <div class="form-card"><div class="form-head"><span class="tag">▯ Form</span><span class="form-code">FP12 / FP14</span></div><div class="form-desc">Supporting Affidavit</div></div>
    <div class="form-card"><div class="form-head"><span class="tag">▯ Form</span><span class="form-code">G7</span></div><div class="form-desc">Information Sheet</div></div>
  </div>
  <div class="form-row wide">
    <div class="form-card"><div class="form-head"><span class="tag">▯ Form</span><span class="form-code">Marriage certificate</span></div><div class="form-desc">Inclusion and document exhibits</div></div>
    <div class="form-card"><div class="form-head"><span class="tag">▯ Form</span><span class="form-code">Child Care</span></div><div class="form-desc">Ceclarations and separation proofs</div></div>
  </div>
  <a class="btn" href="#">See How It Works</a>
</section>

<section class="pricing center">
  <h2 class="section-title">Transparent Pricing. No Hidden Fees.</h2>
  <div class="plans">
    <div class="plan">
      <h3>One-Party Application</h3>
      <p class="for">For applications without spouse consent</p>
      <p class="price">$NZ 299</p>
      <p class="fee">(Government court fee not included)</p>
      <p class="desc">Perfect when you need to proceed without your spouse’s involvement. Includes document automation, human review, and final delivery.</p>
      <a class="btn" href="#">Get Started</a>
    </div>
    <div class="plan featured">
      <h3>Joint Application</h3>
      <p class="for">For applications with spouse consent</p>
      <p class="price">$NZ 249</p>
      <p class="fee">(Government court fee not included)</p>
      <p class="desc">When both parties agree to the dissolution. Includes same features, plus additional court appearance instructions.</p>
      <a class="btn" href="#">Get Started</a>
    </div>
  </div>
  <p class="pay"><strong>Secure Payment Options:</strong> Credit Card, Debit Card, PayLine, WalletPay</p>
  <p class="ssl"><svg width="12" height="13" viewBox="0 0 12 13" fill="none" stroke="var(--green)" stroke-width="1.1"><path d="M6 1l4.5 1.8v3.6c0 2.8-2 4.7-4.5 5.6C3.5 11.1 1.5 9.2 1.5 6.4V2.8z"/><path d="M4 6.6l1.5 1.5 2.8-3"/></svg>Secure checkout with 256-bit SSL encryption</p>
</section>

<section class="faq center">
  <h2 class="section-title">Frequently Asked Questions</h2>
  <div class="faq-list" style="text-align:left">
    <div class="faq-item">
      <div class="faq-q">Do you need to appear in court?<svg width="9" height="9" viewBox="0 0 10 10" fill="none" stroke="#99a" stroke-width="1.2"><path d="M2 6.5l3-3 3 3"/></svg></div>
      <p class="faq-a">Not unless you choose to. We help you opt-out if eligible and guide you through the process of filing without a court appearance in most cases.</p>
    </div>
    <div class="faq-item"><div class="faq-q">Is my information safe?<svg width="9" height="9" viewBox="0 0 10 10" fill="none" stroke="#99a" stroke-width="1.2"><path d="M2 3.5l3 3 3-3"/></svg></div></div>
    <div class="faq-item"><div class="faq-q">Can I apply if I don’t know where my spouse lives?<svg width="9" height="9" viewBox="0 0 10 10" fill="none" stroke="#99a" stroke-width="1.2"><path d="M2 3.5l3 3 3-3"/></svg></div></div>
    <div class="faq-item"><div class="faq-q">How long does it take?<svg width="9" height="9" viewBox="0 0 10 10" fill="none" stroke="#99a" stroke-width="1.2"><path d="M2 3.5l3 3 3-3"/></svg></div></div>
  </div>
</section>

<section class="contact center">
  <h2 class="section-title">Still Have Questions?</h2>
  <p class="sub">We’re here to help—without judgment.</p>
  <div class="contact-grid">
    <div class="contact-item"><svg width="20" height="20" viewBox="0 0 20 20" fill="none" stroke="#334" stroke-width="1.3"><rect x="2" y="4.5" width="16" height="11" rx="1.5"/><path d="M2.5 5.5l7.5 5.5 7.5-5.5"/></svg><h4>Email</h4><p>help@kiwisplit.example</p></div>
    <div class="contact-item"><svg width="20" height="20" viewBox="0 0 20 20" fill="none" stroke="#334" stroke-width="1.3"><path d="M4 2.5h3l1.5 4-2 1.3a10 10 0 0 0 5.7 5.7l1.3-2 4 1.5v3a1.5 1.5 0 0 1-1.6 1.5A15 15 0 0 1 2.5 4.1 1.5 1.5 0 0 1 4 2.5z"/></svg><h4>Phone</h4><p>+64 9 XXX XXXX</p></div>
    <div class="contact-item"><svg width="20" height="20" viewBox="0 0 20 20" fill="none" stroke="#334" stroke-width="1.3"><path d="M4 2.5h3l1.5 4-2 1.3a10 10 0 0 0 5.7 5.7l1.3-2 4 1.5v3a1.5 1.5 0 0 1-1.6 1.5A15 15 0 0 1 2.5 4.1 1.5 1.5 0 0 1 4 2.5z"/></svg><h4>Support Hours</h4><p>Mon–Fri, 9am–5pm NZT</p></div>
  </div>
  <a class="btn" href="#">Start Your Application Today</a>
</section>

<footer class="site-footer center">
  <div class="brand">KiwiSplit</div>
  <nav class="foot-links">
    <a href="#">Application</a><a href="#">How It Works</a><a href="#">FAQs</a><a href="#">Contact</a><a href="#">Privacy Policy</a><a href="#">Terms of Use</a><a href="#">Family Court Info</a>
  </nav>
  <div class="foot-rule"></div>
  <p class="copy">© 2025 KiwiSplit. All rights reserved.</p>
  <p class="disclaimer">This site is not a substitute for legal advice. Consult with a qualified lawyer for complex matters.</p>
</footer>

</body>
</html>
```